Web Design Project for an operational risk management consulting company

Website is for a consulting company specialising in operational risk management. Our specialist areas include crisis and emergency management, community engagement, safety and security. We work internationally, generally in high hazard environments. We are a highly ethical and professional company which prides itself on delivering a strong level of customer service.

As a company we recognise that the key to keeping people safe is ensuring that they work in an ethical and sustainable manner. Therefore we are as much about soft skills as we are about hard skills. We would like our website and supporting images to reflect this.
We have worked throughout Africa and the Middle east, as well as Asia pacific. An international flavour to the website would also be great.
Background images on www.corvellpartnersglobal.example are a good example of what we are thinking of, though very open to fresh ideas.

Target Market(s)

Our customers are generally medium to large organisations who work internationally. We would like to also support more not for profits and non government organisations who work in hazardous environments

Industry/Entity Type

It Company

Number of Pages Required

5+ page

Font styles to use
Sans Serif

Requirements
Must have
• Easy to edit by non IT people
• Section for blogs/news updates
• Pages should include:
• (A) home page
• (B) about us
• (C) services
• (D) contact
• (E) insights
Nice to have
• An international and professional theme. Some gritty images that symbolise the risks associated with working in unstable environments, as well as some human ones and that of the environment
Should not have
• Cartoonish or generic images
• Not focus on traditional physical security aspects

```html
<!DOCTYPE html>
<html lang="en">
<head>
<meta charset="utf-8">
<title>Corvell Partners — Operational Risk Management</title>
<link href="https://fonts.googleapis.com/css2?family=Open+Sans:wght@400;600;700&display=swap" rel="stylesheet">
<style>
:root{
  --blue:#1f6f9e;
  --navy:#1d4f73;
  --orange:#f5a623;
  --text:#555b61;
  --muted:#8a9096;
  --light:#f1f3f5;
  --footer:#e9ecee;
  --line:#dfe3e6;
  --white:#ffffff;
}
*{box-sizing:border-box;margin:0;padding:0}
html,body{width:713px;height:1200px;overflow:hidden}
body{font-family:"Open Sans",Arial,sans-serif;color:var(--text);background:var(--white);font-size:7px;line-height:1.5}
.site-header{height:42px;display:flex;align-items:center;justify-content:space-between;padding:0 40px;background:var(--white)}
.brand{display:flex;align-items:center;gap:6px;font-weight:700;font-size:11px;color:var(--blue)}
.brand-dot{width:16px;height:16px;border-radius:50%;background:var(--blue)}
.main-nav{display:flex;align-self:flex-end}
.main-nav a{display:block;width:60px;text-align:center;padding:10px 0 13px;font-size:6.5px;color:var(--muted);text-decoration:none;border-left:1px solid var(--line)}
.main-nav a.active{color:var(--blue);border-top:2px solid var(--blue)}
.hero{position:relative;height:303px;background:linear-gradient(180deg,#6f8e8a 0%,#8e9a6e 45%,#6d6a3c 75%,#4f5a35 100%);color:var(--white)}
.hero-content{position:absolute;left:222px;top:72px;width:320px}
.hero h1{font-size:14.5px;font-weight:600;line-height:1.35;margin-bottom:8px}
.hero p{font-size:6.5px;line-height:1.55;opacity:.92;margin-bottom:12px}
.btn{display:inline-block;font-size:6px;font-weight:700;text-transform:uppercase;letter-spacing:.5px;padding:4px 10px;text-decoration:none}
.btn-ghost{border:1px solid var(--white);color:var(--white);margin-right:6px;width:70px;text-align:center}
.dots{position:absolute;left:224px;top:196px;display:flex;gap:3px}
.dots span{width:6px;height:6px;border-radius:50%;background:rgba(255,255,255,.5)}
.dots span.on{background:var(--white)}
.about{height:240px;display:flex;padding:55px 0 0 83px;gap:30px}
.about-photo{flex:none;width:190px;height:130px;background:linear-gradient(135deg,#c9ced2,#8c98a3 60%,#5e6b78);border:3px solid var(--white);box-shadow:0 0 0 1px var(--line)}
.about-text{width:300px}
.section-title{font-size:10px;font-weight:600;color:var(--navy);margin-bottom:6px}
.about-text p{font-size:6px;margin-bottom:7px}
.btn-outline{border:1px solid var(--navy);color:var(--navy);margin-top:2px}
.services{position:relative;height:225px;background:var(--blue);color:var(--white)}
.services-head{position:absolute;left:48px;top:24px}
.services-head h2{font-size:9px;font-weight:600}
.services-head small{font-size:5.5px;opacity:.8}
.service-list{position:absolute;left:48px;top:66px;display:flex;gap:22px}
.service{width:200px;display:flex;gap:10px}
.service-icon{flex:none;width:44px;height:44px;border-radius:50%;background:var(--orange);border:3px solid rgba(255,255,255,.75);display:flex;align-items:center;justify-content:center}
.service h3{font-size:7px;font-weight:600;margin-bottom:3px;padding-top:2px}
.service p{font-size:5.5px;opacity:.9;margin-bottom:5px}
.btn-small{border:1px solid var(--white);color:var(--white);padding:2px 8px;font-size:5px}
.updates{height:265px;background:var(--light);display:flex;gap:45px;padding:22px 43px 0}
.col{width:267px}
.col.news{width:310px}
.col-title{display:flex;align-items:center;gap:6px;font-size:8px;font-weight:600;color:var(--navy);margin-bottom:12px}
.col-title i{width:13px;height:13px;border-radius:50%;display:block}
.post{display:flex;gap:8px;background:var(--white);padding:8px;margin-bottom:6px;border:1px solid var(--line)}
.post-thumb{width:26px;height:26px;background:#d6dadd;flex:none}
.post h4,.news-item h4{font-size:6px;color:var(--navy);font-weight:600}
.post .date{font-size:5px;color:var(--blue)}
.post p{font-size:5px;color:var(--muted)}
.news-item{margin-bottom:9px;border-bottom:1px solid var(--line);padding-bottom:5px}
.news-item p{font-size:5px;color:var(--muted)}
.site-footer{height:125px;background:var(--footer);position:relative}
.footer-brand{position:absolute;left:43px;top:22px}
.footer-col{position:absolute;top:22px}
.footer-col h5{font-size:7px;color:var(--navy);font-weight:600;margin-bottom:5px}
.footer-col li{list-style:none;font-size:5.5px;color:var(--muted)}
.social{position:absolute;left:560px;top:24px;display:flex;gap:14px;font-size:5.5px;color:var(--muted)}
.social span{display:flex;align-items:center;gap:3px}
.social i{width:7px;height:7px;border-radius:50%;background:var(--muted);display:block}
.copyright{position:absolute;left:43px;bottom:14px;font-size:5px;color:var(--muted)}
</style>
</head>
<body>
<header class="site-header">
  <div class="brand"><span class="brand-dot"></span>Corvell Partners</div>
  <nav class="main-nav">
    <a class="active" href="#">home page</a><a href="#">about us</a><a href="#">services</a><a href="#">insights</a><a href="#">contact</a>
  </nav>
</header>

<section class="hero" role="img" aria-label="Landscape photograph of a hillside town under a hazy sky">
  <div class="hero-content">
    <h1>Consulting Company Specialising in Operational Risk Management.</h1>
    <p>Our specialist areas include crisis and emergency management, community engagement, safety and security. We work internationally, generally in high hazard environments. We are a highly ethical and professional company which prides itself on delivering a strong level of customer service.</p>
    <a class="btn btn-ghost" href="#">Our services</a><a class="btn btn-ghost" href="#">Insights</a>
  </div>
  <div class="dots"><span class="on"></span><span></span><span></span></div>
</section>

<section class="about">
  <div class="about-photo" role="img" aria-label="Photograph of a team meeting in an office"></div>
  <div class="about-text">
    <h2 class="section-title">about us</h2>
    <p>Phasellus at urna consequat ligula auctor tincidunt. Nunc mollis lorem et lectus sum suscipit. Sed vel hendrerit nisi, eget posuere nisi. Nam rhoncus interdum nisi ac rhoncus. Nullam eleifend nibh. Donec auctor, mauris at suscipit dapibus, elit dictum ultricies mi, vitae tincidunt lorem nulla vel nisl and efficitur ultricies dolor sit amet.</p>
    <p>Fusce accumsan porttitor enim, quis tempor leo. Nunc tincidunt nisl nec cras lacinia pulvinar porttitor urna, tempor ut nisi aliquet massa tempor tristique.</p>
    <a class="btn btn-outline" href="#">Read more</a>
  </div>
</section>

<section class="services">
  <div class="services-head"><h2>core services</h2><small>Our specialist areas</small></div>
  <div class="service-list">
    <div class="service">
      <div class="service-icon"><svg width="18" height="18" viewBox="0 0 16 16"><path d="M6 1h4v5h5v4h-5v5H6v-5H1V6h5z" fill="#fff"/></svg></div>
      <div><h3>Crisis and Emergency Management</h3><p>Phasellus at urna consequat ligula auctor tincidunt. Nunc mollis lorem et lectus dictum ac suscipit.</p><a class="btn btn-small" href="#">More</a></div>
    </div>
    <div class="service">
      <div class="service-icon"><svg width="20" height="18" viewBox="0 0 18 16"><g fill="#fff"><circle cx="9" cy="5" r="3"/><circle cx="3.5" cy="6.5" r="2"/><circle cx="14.5" cy="6.5" r="2"/><path d="M4 15c0-4 2-6 5-6s5 2 5 6z"/><path d="M0 15c0-3 1.5-5 3.5-5 1 0 1.5.3 2 .8C4.5 12 4 13.5 4 15z"/><path d="M18 15c0-3-1.5-5-3.5-5-1 0-1.5.3-2 .8.9 1.2 1.5 2.7 1.5 4.2z"/></g></svg></div>
      <div><h3>Community Engagement</h3><p>Phasellus at urna consequat ligula auctor tincidunt. Nunc mollis lorem et lectus dictum ac suscipit.</p><a class="btn btn-small" href="#">More</a></div>
    </div>
    <div class="service">
      <div class="service-icon"><svg width="16" height="18" viewBox="0 0 14 16"><path d="M3 7V5a4 4 0 0 1 8 0v2" stroke="#fff" stroke-width="2" fill="none"/><rect x="1" y="7" width="12" height="9" rx="1" fill="#fff"/></svg></div>
      <div><h3>Safety and Security</h3><p>Phasellus at urna consequat ligula auctor tincidunt. Nunc mollis lorem et lectus dictum ac suscipit.</p><a class="btn btn-small" href="#">More</a></div>
    </div>
  </div>
</section>

<section class="updates">
  <div class="col">
    <h2 class="col-title"><i style="background:#e05a3a"></i>latest blog</h2>
    <article class="post"><div class="post-thumb"></div><div><h4>Phasellus at urna consequat ligula auctor tincidunt</h4><div class="date">2 weeks ago</div><p>Nunc mollis lorem et lectus dictum ac suscipit, sed vel hendrerit nisi eget posuere.</p></div></article>
    <article class="post"><div class="post-thumb"></div><div><h4>Phasellus at urna consequat ligula auctor tincidunt</h4><div class="date">3 weeks ago</div><p>Nunc mollis lorem et lectus dictum ac suscipit, sed vel hendrerit nisi eget posuere.</p></div></article>
  </div>
  <div class="col news">
    <h2 class="col-title"><i style="background:#8cc152"></i>news updates</h2>
    <div class="news-item"><h4>Phasellus at urna consequat ligula auctor tincidunt</h4><p>Nunc mollis lorem et lectus dictum ac suscipit. Sed vel hendrerit nisi eget posuere nisi nam rhoncus.</p></div>
    <div class="news-item"><h4>Phasellus at urna consequat ligula auctor tincidunt</h4><p>Nunc mollis lorem et lectus dictum ac suscipit. Sed vel hendrerit nisi eget posuere nisi nam rhoncus.</p></div>
    <div class="news-item"><h4>Phasellus at urna consequat ligula auctor tincidunt</h4><p>Nunc mollis lorem et lectus dictum ac suscipit. Sed vel hendrerit nisi eget posuere nisi nam rhoncus.</p></div>
    <div class="news-item"><h4>Phasellus at urna consequat ligula auctor tincidunt</h4><p>Nunc mollis lorem et lectus dictum ac suscipit.</p></div>
  </div>
</section>

<footer class="site-footer">
  <div class="footer-brand"><div class="brand"><span class="brand-dot"></span>Corvell Partners</div></div>
  <div class="footer-col" style="left:210px"><h5>navigations</h5><ul><li>home page</li><li>about us</li><li>services</li><li>insights</li><li>contact</li></ul></div>
  <div class="footer-col" style="left:314px"><h5>Address Info</h5><ul><li>Corvell Partners</li><li>PO Box 4420 Harbour Road</li><li>Northgate 2601</li><li>Australia</li></ul></div>
  <div class="footer-col" style="left:440px"><h5>Contact Info</h5><ul><li>Tel: +61 2 5550 1947</li></ul></div>
  <div class="social"><span><i></i>Friendline</span><span><i></i>Chirpwire</span></div>
  <div class="copyright">© 2015 All rights reserved</div>
</footer>
</body>
</html>
```